Business Card for IT company

I need a high tech looking business card using our logo. I prefer something clean and modern.

Target Market(s)

Buyers of IT hardware and software, IT Techies who are key influencers

Industry/Entity Type

Business

```html
<!DOCTYPE html>
<html lang="en">
<head>
<meta charset="utf-8">
<title>Norvexa Consulting – Business Card</title>
<link rel="stylesheet" href="https://fonts.googleapis.com/css2?family=Open+Sans:wght@400;600;700&display=swap">
<style>
  :root {
    --bg: #e9eaea;
    --card-light: #f4f4f4;
    --card-dark: #2e302f;
    --ink: #1f2120;
    --ink-soft: #7a7c7b;
    --green: #3aa843;
    --white: #ffffff;
    --rule: #c9cbca;
  }
  * { box-sizing: border-box; margin: 0; padding: 0; }
  html, body { width: 1200px; height: 800px; overflow: hidden; }
  body {
    background: var(--bg);
    font-family: "Open Sans", Arial, sans-serif;
    color: var(--ink);
    position: relative;
  }
  .card {
    position: absolute;
    top: 257px;
    width: 500px;
    height: 286px;
    box-shadow: 0 6px 18px rgba(0,0,0,0.12);
  }
  .card--front { left: 70px; background: var(--card-light); }
  .card--back  { left: 630px; background: var(--card-dark); display: flex; align-items: center; justify-content: center; }

  .brand { display: flex; align-items: center; gap: 10px; }
  .brand__mark { width: 14px; height: 14px; background: var(--green); }
  .brand__name { font-weight: 700; font-size: 26px; letter-spacing: 0.5px; }
  .card--front .brand { position: absolute; left: 40px; top: 52px; }
  .card--front .brand__name { color: var(--ink); }
  .card--back .brand__name { color: var(--white); font-size: 30px; }
  .card--back .brand__mark { width: 16px; height: 16px; }

  .divider { position: absolute; left: 232px; top: 126px; }

  .person { position: absolute; left: 40px; bottom: 40px; display: flex; align-items: flex-start; gap: 10px; }
  .person__marker { width: 0; height: 0; border-left: 11px solid var(--green); border-top: 6px solid transparent; border-bottom: 6px solid transparent; margin-top: 5px; transform: rotate(-90deg); }
  .person__name { font-weight: 700; font-size: 17px; }
  .person__role { font-weight: 600; font-size: 11px; color: var(--green); }

  .contact { position: absolute; right: 30px; top: 42px; text-align: right; font-size: 11px; line-height: 1.4; }
  .contact__address { margin-bottom: 8px; }
  .contact__line { display: flex; justify-content: flex-end; align-items: center; gap: 6px; }
  .contact__icon { width: 11px; height: 11px; background: var(--ink); border-radius: 2px; display: inline-flex; }
  .contact__icon svg { width: 11px; height: 11px; }
</style>
</head>
<body>
  <section class="card card--front" aria-label="Business card front">
    <div class="brand">
      <span class="brand__mark"></span>
      <span class="brand__name">Norvexa Consulting</span>
    </div>

    <svg class="divider" width="70" height="40" aria-hidden="true">
      <line x1="0" y1="0" x2="70" y2="40" stroke="var(--rule)" stroke-width="1"/>
    </svg>

    <div class="person">
      <span class="person__marker"></span>
      <div>
        <p class="person__name">Alex Morgan</p>
        <p class="person__role">Founder</p>
      </div>
    </div>

    <address class="contact" style="font-style: normal;">
      <p class="contact__address">820 Harbor Point Drive<br>Suite 400<br>Easton, MD 21601</p>
      <p class="contact__line">555.014.2290
        <span class="contact__icon"><svg viewBox="0 0 11 11"><path d="M3 2.5 L4.5 4 L3.8 5 Q5 7 6.5 7.5 L7.3 6.8 L8.7 8.2 L7.8 9 Q4 8.5 2.2 3.6 Z" fill="#fff"/></svg></span>
      </p>
      <p class="contact__line">info@norvexa.com
        <span class="contact__icon"><svg viewBox="0 0 11 11"><rect x="2" y="3" width="7" height="5" fill="none" stroke="#fff" stroke-width="0.9"/><path d="M2 3 L5.5 6 L9 3" fill="none" stroke="#fff" stroke-width="0.9"/></svg></span>
      </p>
      <p class="contact__line">www.norvexa.com
        <span class="contact__icon"><svg viewBox="0 0 11 11"><circle cx="5.5" cy="5.5" r="3.2" fill="none" stroke="#fff" stroke-width="0.9"/><line x1="2.3" y1="5.5" x2="8.7" y2="5.5" stroke="#fff" stroke-width="0.8"/><ellipse cx="5.5" cy="5.5" rx="1.4" ry="3.2" fill="none" stroke="#fff" stroke-width="0.8"/></svg></span>
      </p>
    </address>
  </section>

  <section class="card card--back" aria-label="Business card back">
    <div class="brand">
      <span class="brand__mark"></span>
      <span class="brand__name">Norvexa Consulting</span>
    </div>
  </section>
</body>
</html>
```